Environmental Health Survey for Medical Providers in Indiana

I am sending out an environmental health survey to all health care providers (MDs, NPs, and DOs) in Indiana to assess their knowledge of environmental health concerns that effect their patients. Based on that assessment, I will then send them targeted free continuing education modules to bolster their knowledge in any weak points. The postcard will have a website link on it that they will go to for the survey (I wish I could email them, but Indiana doesn't collect provider emails, only addresses). I need to somehow pull these providers in to complete my survey and get the free CEs. This is for my doctorate thesis. The survey link is: http://shortlinkr.example/surveyquo

Target Market(s)

Nurse Practitioners, Medical Doctors, and Doctors of Osteopathic Medicine in Indiana.

Industry/Entity Type

Health Care

Colors
00a990
33b8a4

Requirements
Must have
• 1. A space for addresses & postage, as these will be mailed.
• 2. The survey link

```html
<!DOCTYPE html>
<html lang="en">
<head>
<meta charset="utf-8">
<title>Environmental Health Survey Postcard</title>
<link rel="stylesheet" href="https://fonts.googleapis.com/css2?family=Oswald:wght@400;500&family=Ubuntu:wght@400;500&family=Open+Sans:ital,wght@0,600;1,400&family=Dancing+Script:wght@700&display=swap">
<style>
  :root {
    --green: #12a84a;
    --green-light: #5cc24e;
    --green-pale: #e8f3e2;
    --ink: #1e1e1e;
    --silver: #c9cdcf;
    --stamp: #d9d9d9;
    --rule: #9a9a9a;
    --page: #e6e6e6;
  }
  * { margin: 0; padding: 0; box-sizing: border-box; }
  html, body { width: 1200px; height: 1200px; overflow: hidden; background: var(--page); }
  .postcard {
    position: absolute;
    left: 197px;
    width: 805px;
    height: 546px;
    overflow: hidden;
    background: #fff;
  }
  .postcard--front { top: 36px; }
  .postcard--back { top: 618px; }
  .postcard svg { position: absolute; inset: 0; }

  .headline {
    position: absolute;
    left: 36px;
    font-family: "Oswald", sans-serif;
    color: #fff;
    line-height: 1;
    text-shadow: 0 2px 3px rgba(0,0,0,.25);
  }
  .headline__lead { display: block; font-size: 30px; font-weight: 400; margin-top: 58px; letter-spacing: .2px; }
  .headline__state { display: block; font-size: 80px; font-weight: 500; margin-top: 4px; letter-spacing: -.5px; }

  .laptop-screen {
    position: absolute;
    background: #fff;
    border: 9px solid #111;
    border-radius: 4px;
    display: flex;
    flex-direction: column;
    justify-content: center;
    align-items: center;
    font-family: "Oswald", sans-serif;
    line-height: 1;
  }
  .laptop-screen__small { color: var(--ink); }
  .laptop-screen__big { color: var(--green); font-weight: 500; }
  .postcard--front .laptop-screen { left: 56px; top: 310px; width: 230px; height: 153px; }
  .postcard--front .laptop-screen__small { font-size: 31px; }
  .postcard--front .laptop-screen__big { font-size: 50px; margin-top: 2px; }
  .postcard--back .laptop-screen { left: 82px; top: 262px; width: 184px; height: 121px; border-width: 8px; }
  .postcard--back .laptop-screen__small { font-size: 25px; }
  .postcard--back .laptop-screen__big { font-size: 40px; margin-top: 2px; }

  .cta { position: absolute; font-family: "Ubuntu", sans-serif; font-weight: 500; line-height: 1; }
  .postcard--front .cta { left: 342px; top: 406px; font-size: 40px; color: var(--green); }
  .postcard--back .cta { left: 36px; top: 415px; font-size: 34px; color: #fff; }

  .survey-link { position: absolute; font-family: "Open Sans", sans-serif; font-weight: 600; line-height: 1; white-space: nowrap; }
  .postcard--front .survey-link { left: 408px; top: 456px; font-size: 21px; color: var(--ink); }
  .postcard--back .survey-link { left: 89px; top: 457px; font-size: 18px; color: #fff; }

  .intro-title {
    position: absolute; left: 30px; top: 32px;
    font-family: "Dancing Script", cursive; font-weight: 700;
    font-size: 32px; color: var(--green); line-height: 1;
  }
  .intro-text {
    position: absolute; left: 32px; top: 80px; width: 352px;
    font-family: "Open Sans", sans-serif; font-style: italic;
    font-size: 11.6px; line-height: 16px; color: var(--ink);
    text-align: justify;
  }
</style>
</head>
<body>

<section class="postcard postcard--front">
  <svg viewBox="0 0 805 546" width="805" height="546">
    <defs>
      <linearGradient id="frontWash" x1="0" y1="0" x2="0" y2="1">
        <stop offset="0" stop-color="#dff0d6"/>
        <stop offset="1" stop-color="#f7faf5"/>
      </linearGradient>
      <linearGradient id="parkScene" x1="0" y1="0" x2="0" y2="1">
        <stop offset="0" stop-color="#b9cfd6"/>
        <stop offset=".35" stop-color="#5f8a2e"/>
        <stop offset=".75" stop-color="#7fae3a"/>
        <stop offset="1" stop-color="#e6f0dc"/>
      </linearGradient>
      <linearGradient id="greenPanel" x1="0" y1="0" x2="1" y2="1">
        <stop offset="0" stop-color="#2faa3f"/>
        <stop offset="1" stop-color="#5cc24e"/>
      </linearGradient>
      <radialGradient id="medPhoto" cx=".5" cy=".5" r=".6">
        <stop offset="0" stop-color="#eef5fb"/>
        <stop offset="1" stop-color="#9fc3dc"/>
      </radialGradient>
    </defs>
    <rect width="805" height="546" fill="url(#frontWash)"/>
    <rect x="395" y="0" width="410" height="320" fill="url(#parkScene)" role="img" aria-label="Sunlit park with green trees and lawn"/>
    <path d="M0,0 H405 C440,45 445,175 385,245 C335,285 200,260 120,236 C70,220 30,206 0,196 Z" fill="#d7dadb"/>
    <path d="M0,0 H400 C430,40 435,165 378,232 C330,270 200,248 120,222 C70,206 30,192 0,182 Z" fill="url(#greenPanel)"/>

    <g role="img" aria-label="Tablet showing a heart monitor with a stethoscope">
      <circle cx="379" cy="308" r="72" fill="var(--green-light)"/>
      <circle cx="379" cy="308" r="64" fill="url(#medPhoto)"/>
    </g>
    <g role="img" aria-label="Hand holding a stethoscope with medical icons">
      <circle cx="543" cy="308" r="80" fill="var(--green-light)"/>
      <circle cx="543" cy="308" r="72" fill="url(#medPhoto)"/>
    </g>
    <g role="img" aria-label="Stethoscope resting on a heart rate chart">
      <circle cx="705" cy="308" r="72" fill="var(--green-light)"/>
      <circle cx="705" cy="308" r="64" fill="url(#medPhoto)"/>
    </g>

    <path d="M27,466 H316 L310,476 H33 Z" fill="#bfc2c4"/>
    <path d="M386,446 c-10,6 -14,14 -10,24 l-5,0 l9,10 l9,-10 l-5,0 c-3,-8 -1,-16 2,-24 z" fill="var(--green)" transform="rotate(40 382 464)"/>

    <rect x="0" y="500" width="805" height="4" fill="#fff"/>
    <rect x="0" y="504" width="805" height="42" fill="var(--green)"/>
    <path d="M0,510 H470 C515,510 535,526 555,546 H0 Z" fill="#1b1b1b"/>
  </svg>
  <h1 class="headline">
    <span class="headline__lead">ALL HEALTH CARE PROVIDERS</span>
    <span class="headline__state">IN INDIANA</span>
  </h1>
  <div class="laptop-screen">
    <span class="laptop-screen__small">Free continuing</span>
    <span class="laptop-screen__big">Education</span>
  </div>
  <p class="cta">Join our survey here:</p>
  <p class="survey-link">http://shortlinkr.example/surveyquo</p>
</section>

<section class="postcard postcard--back">
  <svg viewBox="0 0 805 546" width="805" height="546">
    <defs>
      <linearGradient id="backWash" x1="0" y1="0" x2="1" y2="1">
        <stop offset="0" stop-color="#d6ecc9"/>
        <stop offset="1" stop-color="#f5f9f2"/>
      </linearGradient>
      <linearGradient id="backGreen" x1="0" y1="0" x2="1" y2="1">
        <stop offset="0" stop-color="#1fa843"/>
        <stop offset="1" stop-color="#5cc24e"/>
      </linearGradient>
      <radialGradient id="doctorPhoto" cx=".5" cy=".5" r=".6">
        <stop offset="0" stop-color="#ffffff"/>
        <stop offset="1" stop-color="#cfdde6"/>
      </radialGradient>
    </defs>
    <path d="M0,0 H440 C415,80 428,150 440,205 C452,300 428,420 418,500 H0 Z" fill="var(--green-light)"/>
    <path d="M0,0 H425 C402,80 414,150 426,205 C438,300 414,420 404,500 H0 Z" fill="#d4d8d9"/>
    <path d="M0,0 H418 C395,80 407,150 419,205 C431,300 407,420 397,500 H0 Z" fill="url(#backWash)"/>
    <path d="M0,222 C120,194 260,190 330,206 L330,218 C260,204 120,210 0,236 Z" fill="#1b1b1b"/>
    <path d="M0,236 C120,210 260,204 330,218 C400,232 436,266 430,330 C424,400 410,460 404,500 H0 Z" fill="url(#backGreen)"/>

    <g role="img" aria-label="Doctor in a white coat holding a tablet">
      <circle cx="391" cy="250" r="86" fill="#fff" stroke="#666" stroke-width="3"/>
      <circle cx="391" cy="250" r="76" fill="url(#doctorPhoto)" stroke="var(--green-light)" stroke-width="2"/>
    </g>

    <path d="M58,386 H290 L284,395 H64 Z" fill="#bfc2c4"/>
    <path d="M70,446 c-9,5 -13,12 -9,21 l-5,0 l8,9 l8,-9 l-5,0 c-3,-7 -1,-14 2,-21 z" fill="#1b1b1b" transform="rotate(40 66 461)"/>

    <rect x="684" y="29" width="85" height="84" fill="var(--stamp)"/>
    <g stroke="var(--rule)" stroke-width="1.2">
      <line x1="520" y1="261" x2="759" y2="261"/>
      <line x1="520" y1="315" x2="759" y2="315"/>
      <line x1="520" y1="370" x2="759" y2="370"/>
      <line x1="520" y1="421" x2="759" y2="421"/>
    </g>

    <rect x="0" y="500" width="805" height="4" fill="#fff"/>
    <rect x="0" y="504" width="805" height="42" fill="var(--green)"/>
    <path d="M0,510 H470 C515,510 535,526 555,546 H0 Z" fill="#1b1b1b"/>
  </svg>
  <h2 class="intro-title">This is a voluntary survey</h2>
  <p class="intro-text">to help you better understand the environmental aspects of healthcare and behaviors that effect your patient population. After taking this survey, you will be directed to select various free CE modules to help bolster your knowledge on topics addressed in the survey.</p>
  <div class="laptop-screen">
    <span class="laptop-screen__small">Free continuing</span>
    <span class="laptop-screen__big">Education</span>
  </div>
  <p class="cta">Join our survey here:</p>
  <p class="survey-link">http://shortlinkr.example/surveyquo</p>
</section>

</body>
</html>
```